use the existing webpage www.lyravelbeauty.ch an create a modern style page using the same logos pictures and text . t
Target Market(s)
healthcare and cosmetigs
Number of Pages Required
1 page
Requirements
Must have
- same cooperate identity and style as the original lyravelbeauty.ch
- a link to the webshop: https://www.lyravelbeauty.webstores.ch/ (no new window)
- ignore evntual text written in polish language.

```html
<!DOCTYPE html>
<html lang="en">
<head>
<meta charset="utf-8">
<title>Lyravel Beauty – High Quality Cosmetics</title>
<link href="https://fonts.googleapis.com/css2?family=Lato:wght@400;700;900&family=Open+Sans:wght@400;600;700&display=swap" rel="stylesheet">
<style>
:root{
  --gold:#8b7748;
  --gold-light:#a38f5c;
  --black:#000;
  --ink:#111;
  --text:#555;
  --grey-bg:#f4f4f4;
  --white:#fff;
}
*{box-sizing:border-box;margin:0;padding:0}
html,body{width:1200px;height:3082px;overflow:hidden}
body{position:relative;font-family:'Open Sans',sans-serif;color:var(--text);background:var(--white)}
a{text-decoration:none;color:inherit}
.abs{position:absolute}
.btn{position:absolute;display:flex;align-items:center;justify-content:center;background:var(--gold);color:var(--white);font-family:'Open Sans',sans-serif;font-weight:700;font-size:14px;letter-spacing:.3px}
.brand{font-family:'Open Sans',sans-serif;font-weight:400;color:var(--gold);font-size:24px;letter-spacing:5px;display:flex;align-items:center;gap:12px}
.brand .mark{width:14px;height:14px;border:2px solid var(--gold)}
/* header */
.site-header{left:0;top:0;width:1200px;height:92px;background:var(--black)}
.site-header .brand{position:absolute;left:98px;top:30px}
.main-nav{position:absolute;right:98px;top:32px;display:flex;font-size:14px;font-weight:600;color:var(--gold-light)}
.main-nav a{padding:6px 10px;line-height:18px}
.main-nav a.active{background:var(--gold);color:var(--white)}
/* hero */
.hero{left:0;top:92px;width:1200px;height:544px;background:linear-gradient(180deg,#8d8d90 0%,#c4c4c6 55%,#e2e2e3 100%);overflow:hidden}
.hero-photo{position:absolute;left:560px;top:90px;width:640px;height:454px;background:linear-gradient(160deg,#3a3a3c 0%,#111 55%,#2b2418 100%);border-radius:4px 0 0 0}
.hero-text{position:absolute;left:98px;top:96px;width:440px}
.hero h1{font-family:'Lato',sans-serif;font-weight:900;font-size:40px;line-height:48px;color:var(--gold)}
.hero p{margin-top:18px;font-family:'Open Sans',sans-serif;font-weight:600;font-size:21px;line-height:37px;color:#1c1c1c}
.hero .btn{left:98px;top:278px;width:190px;height:46px;font-size:16px}
/* intro */
.intro{left:0;top:636px;width:1200px;height:446px;text-align:center}
.intro h2{margin-top:82px;font-family:'Lato',sans-serif;font-weight:900;font-size:29px;color:var(--ink)}
.intro h3{margin-top:30px;font-family:'Open Sans',sans-serif;font-weight:600;font-size:17px;color:var(--gold)}
.intro p{width:760px;margin:22px auto 0;font-size:13px;line-height:23px}
.intro .btn{left:526px;top:312px;width:147px;height:40px}
/* products */
.products{left:0;top:1082px;width:1200px;height:1090px;background:var(--grey-bg)}
.product-photo{position:absolute;width:458px;height:260px;border:4px solid var(--white);box-shadow:0 0 2px rgba(0,0,0,.2)}
.product-title{position:absolute;font-family:'Lato',sans-serif;font-weight:900;font-size:29px;color:var(--ink);white-space:nowrap}
.product-text{position:absolute;width:472px;font-size:13px;line-height:23px;text-align:justify}
.products .btn{width:158px;height:40px}
/* testimonial */
.testimonial{left:0;top:2172px;width:1200px;height:440px;text-align:center}
.quote-badge{position:absolute;left:522px;top:86px;width:96px;height:96px;border-radius:50%;background:var(--gold);display:flex;align-items:center;justify-content:center;padding-right:20px}
.avatar{position:absolute;left:578px;top:84px;width:100px;height:100px;border-radius:50%;border:4px solid var(--white);background:linear-gradient(160deg,#9c8a82,#4a3b36)}
.testimonial blockquote{position:absolute;left:210px;top:220px;width:780px;font-size:14px;line-height:30px}
.testimonial .author{position:absolute;left:0;width:1200px;top:328px;font-size:13px}
.testimonial .author strong{font-family:'Lato',sans-serif;font-weight:900;font-size:18px;color:#333;letter-spacing:.5px}
.arrow{position:absolute;top:224px}
/* newsletter */
.newsletter{left:0;top:2612px;width:1200px;height:178px;background:linear-gradient(90deg,#7d6a3f 0%,#a08b58 50%,#806d43 100%)}
.newsletter h2{position:absolute;left:98px;top:52px;font-family:'Lato',sans-serif;font-weight:900;font-size:29px;color:var(--white)}
.newsletter p{position:absolute;left:98px;top:108px;font-size:12px;color:var(--white)}
.newsletter .email{position:absolute;left:675px;top:71px;width:320px;height:40px;background:var(--white);font-size:12px;color:#444;padding:12px 14px}
.newsletter .subscribe{position:absolute;left:995px;top:71px;width:105px;height:40px;background:var(--black);color:var(--white);font-weight:700;font-size:14px;display:flex;align-items:center;justify-content:center}
/* footer */
.site-footer{left:0;top:2790px;width:1200px;height:292px;background:var(--black)}
.site-footer .brand{position:absolute;left:98px;top:100px}
.footer-col h4{position:absolute;font-family:'Open Sans',sans-serif;font-weight:400;font-size:14px;color:var(--gold-light);letter-spacing:.5px}
.contact-line{position:absolute;left:573px;display:flex;align-items:center;gap:18px;font-size:14px;color:var(--gold-light)}
.socials{position:absolute;left:948px;top:120px;display:flex;gap:10px}
.socials span{width:30px;height:30px;border:1.5px solid var(--gold-light);border-radius:50%}
.site-footer hr{position:absolute;left:98px;top:220px;width:1002px;border:0;border-top:1px solid #3a3a3a}
.copyright{position:absolute;left:0;top:250px;width:1200px;text-align:center;font-size:13px;color:var(--gold-light)}
</style>
</head>
<body>

<header class="abs site-header">
  <a class="brand" href="#"><span class="mark"></span>Lyravel Beauty</a>
  <nav class="main-nav">
    <a class="active" href="#">HOME</a>
    <a href="#">ABOUT US</a>
    <a href="#">CLINICAL EXAMINATIONS</a>
    <a href="#">PRODUCTS</a>
    <a href="#">BUSINESS</a>
    <a href="#">CONTACT</a>
  </nav>
</header>

<section class="abs hero">
  <div class="hero-photo" role="img" aria-label="Black and gold product boxes: eyelash serum, volumizing mascara and hair conditioner bottle"></div>
  <div class="hero-text">
    <h1>LYRAVEL BEAUTY</h1>
    <p>Are You Looking For The Best Serum<br>For Your yelashes?</p>
  </div>
  <a class="btn" href="https://www.lyravelbeauty.webstores.ch/">BUY IN OUR SHOP</a>
</section>

<section class="abs intro">
  <h2>HIGH QUALITY COSMETICS</h2>
  <h3>Are You Looking For The Best Serum For Your Eyelashes?</h3>
  <p>Effectiveness, fast effect, or maybe high quality? These are just some of the features that should make a GOOD EYELASH SERUM .When using a particular product, we have high expectations for this product. RENEWA FOR EYELASHES IT should extend, make denser and nourish. It is also important to strengthen short and weak eyelashes.</p>
  <a class="btn" href="#">READ MORE
    <svg width="13" height="13" viewBox="0 0 14 14" style="margin-left:5px"><circle cx="7" cy="7" r="7" fill="#fff"/><path d="M5.5 4l3 3-3 3" stroke="#8b7748" stroke-width="1.8" fill="none"/></svg></a>
</section>

<section class="abs products">
  <div class="product-photo" style="left:98px;top:85px;background:linear-gradient(150deg,#e9e9e9,#1a1a1a 45%,#2a2a2a 80%,#ddd)" role="img" aria-label="Eyelash serum in open black box on white fur"></div>
  <h2 class="product-title" style="left:627px;top:70px">AURELLE EYELASH</h2>
  <p class="product-text" style="left:627px;top:144px">The uniqueness and effectiveness of the product, which can already be observed after 15 days of regular use, ensures a complex of substances that complement each other. An excellent result is already achieved after 15 days of regular use, the maximum phase of the cure takes place after 2-3 months. During this time, the serum is applied once daily and maintain the result.</p>
  <a class="btn" style="left:627px;top:300px" href="https://www.lyravelbeauty.webstores.ch/">BUY IN OUR SHOP</a>

  <h2 class="product-title" style="left:98px;top:404px">VELORA VOLUMIZING MASCARA</h2>
  <p class="product-text" style="left:98px;top:478px">The uniqueness and effectiveness of the product, which can already be observed after 15 days of regular use, ensures a complex of substances that complement each other. An excellent result is already achieved after 15 days of regular use, the maximum phase of the cure takes place after 2-3 months. During this time, the serum is applied once daily and maintain the result.</p>
  <a class="btn" style="left:98px;top:635px" href="https://www.lyravelbeauty.webstores.ch/">BUY IN OUR SHOP</a>
  <div class="product-photo" style="left:641px;top:415px;background:linear-gradient(160deg,#c7b48a,#2a2a2a 40%,#151515 75%,#c4542d)" role="img" aria-label="Volumizing mascara in open black box beside orange flowers"></div>

  <div class="product-photo" style="left:98px;top:750px;background:linear-gradient(110deg,#e8e6e3 0%,#d9cfc9 35%,#1c1c1c 60%,#2a2a2a 85%,#efefef)" role="img" aria-label="Hair conditioner bottle and black box with carnations"></div>
  <h2 class="product-title" style="left:627px;top:740px">HAIR CONDITIONER</h2>
  <p class="product-text" style="left:627px;top:814px">The uniqueness and effectiveness of the product, which can already be observed after 15 days of regular use, ensures a complex of substances that complement each other. An excellent result is already achieved after 15 days of regular use, the maximum phase of the cure takes place after 2-3 months. During this time, the serum is applied once daily and maintain the result.</p>
  <a class="btn" style="left:627px;top:970px" href="https://www.lyravelbeauty.webstores.ch/">BUY IN OUR SHOP</a>
</section>

<section class="abs testimonial">
  <div class="quote-badge"><svg width="38" height="30" viewBox="0 0 38 30"><path d="M2 28V16C2 8 6 3 14 1l1 4c-5 2-6 5-6 9h6v14zM22 28V16c0-8 4-13 12-15l1 4c-5 2-6 5-6 9h6v14z" fill="#fff"/></svg></div>
  <div class="avatar" role="img" aria-label="Customer portrait"></div>
  <svg class="arrow" style="left:42px" width="14" height="24" viewBox="0 0 14 24"><path d="M12 2L2 12l10 10" stroke="#777" stroke-width="2" fill="none"/></svg>
  <svg class="arrow" style="left:1144px" width="14" height="24" viewBox="0 0 14 24"><path d="M2 2l10 10L2 22" stroke="#777" stroke-width="2" fill="none"/></svg>
  <blockquote>At vero eos et accusamus et iusto odio dignissimos ducimus qui blanditiis praesentium voluptatum deleniti atque corrupti quos dolores et quas molestias excepturi sint occaecati cupiditate non provident, similique sunt in culpa officia deserunt mollitia animi, id est laborum et dolorum fuga. Et harum quidem rerum facilis.</blockquote>
  <p class="author"><strong>ELENA VARGA</strong>, Northwind Studio AG.</p>
</section>

<section class="abs newsletter">
  <h2>NEED MORE DETAILS?</h2>
  <p>We are here to assist. Contact us by phone, email or via our Social Media...</p>
  <div class="email">Enter Email</div>
  <div class="subscribe">SUBSCRIBE</div>
</section>

<footer class="abs site-footer">
  <a class="brand" href="#"><span class="mark"></span>Lyravel Beauty</a>
  <div class="footer-col">
    <h4 style="left:573px;top:72px">CONTACT US</h4>
    <div class="contact-line" style="top:112px"><svg width="16" height="16" viewBox="0 0 24 24"><path d="M6.6 10.8a15 15 0 006.6 6.6l2.2-2.2c.3-.3.7-.4 1-.2 1.1.4 2.3.6 3.6.6.6 0 1 .4 1 1V20c0 .6-.4 1-1 1A17 17 0 013 4c0-.6.4-1 1-1h3.5c.6 0 1 .4 1 1 0 1.3.2 2.5.6 3.6.1.3 0 .7-.2 1z" fill="#a38f5c"/></svg>(+41) 22 555 0147</div>
    <div class="contact-line" style="top:150px"><svg width="16" height="14" viewBox="0 0 16 12"><rect width="16" height="12" fill="#a38f5c"/><path d="M0 0l8 6 8-6" stroke="#000" stroke-width="1.3" fill="none"/></svg>info@lyravelbeauty.ch</div>
    <h4 style="left:948px;top:72px">SOCIAL MEDIA</h4>
    <div class="socials"><span></span><span></span><span></span><span></span></div>
  </div>
  <hr>
  <p class="copyright">© Copyright 2018 Lyravel Beauty. All Rights Reserved &nbsp;|&nbsp; Privacy Policy.</p>
</footer>

</body>
</html>
```